BRANWELL LAW FIRM

Seeking a business logo and business card design incorporating the logo. We have an existing business card (attached), which we would like redesigned incorporating the new logo and existing text (front and back). Also, logo and business card should incorporate the same color scheme as on the attached. There are several employees who will need business cards; not sure how this is handled from a business card design standpoint . . . please contact me with any questions/concerns.

Please feel free to redesign front of business card. Branwell Law Firm must read Branwell Law Firm, P.C.

Back of business card should have the below address information towards the bottom of the card, so there is room for someone to write on the back. The address information on the back of the business cards is as follows:

Three Galton Court Plaza
2700 Marrow Boulevard, Suite 3040
Philadelphia, PA 19999
T: (215) 555.0143

68 Tilbury Avenue, 24th Floor
New York, NY 10099
T: (212) 555-0188

Industry/Entity Type

Business

Logo Text

BLF

```html
<!DOCTYPE html>
<html lang="en">
<head>
<meta charset="utf-8">
<title>Branwell Law Firm, P.C. — Logo and Business Card</title>
<link rel="stylesheet" href="https://fonts.googleapis.com/css2?family=Marcellus+SC&display=swap">
<style>
  :root {
    --ink: #333d4f;
    --card: #333d4f;
    --card-text: #babdc3;
    --card-rule: #a6a9b0;
    --paper: #ffffff;
  }
  html, body {
    margin: 0;
    padding: 0;
    overflow: hidden;
    background: var(--paper);
  }
  .sheet {
    position: relative;
    width: 981px;
    height: 1200px;
    overflow: hidden;
    background: var(--paper);
    font-family: "Marcellus SC", serif;
  }
  .line {
    position: absolute;
    left: 0;
    right: 0;
    margin: 0;
    text-align: center;
    white-space: nowrap;
    font-style: normal;
  }

  /* Primary logo */
  .brand-logo { position: absolute; left: 0; top: 0; width: 981px; height: 340px; color: var(--ink); }
  .brand-logo .brand-name { top: 196px; font-size: 70px; letter-spacing: 12px; line-height: 80px; }
  .brand-logo .brand-suffix { top: 284px; font-size: 31px; letter-spacing: 5px; line-height: 36px; }

  /* Cards */
  .card {
    position: absolute;
    left: 192px;
    width: 599px;
    height: 335px;
    background: var(--card);
    color: var(--card-text);
  }
  .card-front { top: 386px; }
  .card-back { top: 763px; }
  .card-frame {
    position: absolute;
    left: 10px;
    right: 10px;
    border: 2px solid var(--card-rule);
  }
  .card-front .card-frame { top: 11px; height: 238px; }
  .card-back .card-frame { top: 109px; height: 211px; }

  .card-front .brand-name { top: 75px; font-size: 38px; letter-spacing: 6px; line-height: 40px; }
  .card-front .brand-suffix { top: 110px; font-size: 17px; letter-spacing: 1.5px; line-height: 22px; }
  .card-front .person-name { top: 146px; font-size: 33px; letter-spacing: 2.5px; line-height: 36px; }
  .card-front .person-title { top: 177px; font-size: 11px; letter-spacing: 1.2px; line-height: 14px; }
  .card-front .person-email { top: 210px; font-size: 17px; letter-spacing: 1.6px; line-height: 24px; }

  .card-offices, .card-contact {
    position: absolute;
    top: 270px;
    width: 240px;
    text-align: center;
    font-size: 16px;
    letter-spacing: 1.8px;
    line-height: 20px;
  }
  .card-offices { left: 14px; }
  .card-contact { left: 309px; width: 240px; }
  .card-contact p, .card-offices p { margin: 0; white-space: nowrap; }
  .card-divider {
    position: absolute;
    left: 257px;
    top: 266px;
    width: 2px;
    height: 50px;
    background: var(--card-rule);
  }

  .card-back .address { font-size: 18px; letter-spacing: 2px; line-height: 23.5px; font-style: normal; }
  .card-back .address-philadelphia { top: 124px; }
  .card-back .address-newyork { top: 235px; }
  .card-back .address p { margin: 0; }
  .card-back .address-rule {
    position: absolute;
    left: 180px;
    top: 225px;
    width: 239px;
    height: 2px;
    background: var(--card-rule);
  }
</style>
</head>
<body>
<main class="sheet">

  <section class="brand-logo" aria-label="Branwell Law Firm, P.C. logo">
    <p class="line brand-name">BRANWELL</p>
    <p class="line brand-suffix">LAW FIRM, P.C.</p>
  </section>

  <section class="card card-front" aria-label="Business card front">
    <div class="card-frame"></div>
    <p class="line brand-name">BRANWELL</p>
    <p class="line brand-suffix">Law Firm, P.C.</p>
    <p class="line person-name">Dorian M. Weller</p>
    <p class="line person-title">Director Business Development</p>
    <p class="line person-email">dweller@branwelllawfirm.com</p>
    <div class="card-offices">
      <p>Philadelphia,PA</p>
      <p>New York, NY</p>
    </div>
    <div class="card-divider"></div>
    <div class="card-contact">
      <p>215-555-0127 mobile</p>
      <p>www.branwelllawfirm.com</p>
    </div>
  </section>

  <section class="card card-back" aria-label="Business card back">
    <div class="card-frame"></div>
    <address class="line address address-philadelphia">
      <p>Three Galton Court Plaza</p>
      <p>2700 Marrow Boulevard, Suite 3040</p>
      <p>Philadelphia, PA 19999</p>
      <p>T: (215) 555.0143</p>
    </address>
    <div class="address-rule"></div>
    <address class="line address address-newyork">
      <p>68 Tilbury Avenue, 24th Floor</p>
      <p>New York, NY 10099</p>
      <p>T: (212) 555-0188</p>
    </address>
  </section>

</main>
</body>
</html>
```